Fun Trendy High End Spa Services
Business Card, Gift Certificate, Gift Certificate Envelope
I need double sided standard sized Business Card [3.5" x 2"]
We like what is in logo that was uploaded but please use your creativity. We are open to any ideas.
Simple
Lena Harbus LMT
Owner
Mobile
BP@BrightPebblo.com
BrightPebblo.com
We are open to all concepts. So please be creative. This is for Very high end spa service so it needs to look very good. We thought black paper for a base on business cards, gift certificate and GC envelope but are open to any and all ideas! Thank You! We will pick a winner early if we find the perfect design.
"The greatest wealth is health"
(Doesnt need " " on there just use your own idea and play with it.)
Here is The winning logo design. We really like the style but please feel free to be creative with it! Thank you so much!
This is the style of gift certificate that we want designed to match our business card.

```html
<!DOCTYPE html>
<html lang="en">
<head>
<meta charset="utf-8">
<title>Bright Pebblo – Business Card</title>
<link rel="stylesheet" href="https://fonts.googleapis.com/css2?family=Tinos&family=Arimo&display=swap">
<style>
  :root {
    --backdrop: #9a9a9a;
    --card: #231f20;
    --silver: #d4d4d4;
    --silver-dark: #a9a9a9;
    --gold: #e2a42a;
    --ink: #111111;
  }
  * { box-sizing: border-box; }
  html, body {
    margin: 0;
    padding: 0;
    width: 1200px;
    height: 871px;
    overflow: hidden;
    background: var(--backdrop);
    position: relative;
  }
  .card {
    position: absolute;
    left: 302px;
    width: 586px;
    background: var(--card);
    border-radius: 22px;
    overflow: hidden;
  }
  .card--front { top: 98px; height: 368px; }
  .card--back { top: 530px; height: 270px; }

  .brand {
    position: absolute;
    left: 130px;
    top: 14px;
    display: flex;
    align-items: center;
    gap: 24px;
  }
  .brand__dot {
    width: 80px;
    height: 80px;
    border-radius: 50%;
    background: var(--silver-dark);
  }
  .brand__name {
    font-family: "Arimo", sans-serif;
    font-size: 44px;
    line-height: 44px;
    color: var(--silver);
    margin: 0;
  }
  .person {
    position: absolute;
    left: 0;
    right: 0;
    top: 164px;
    text-align: center;
    font-family: "Tinos", serif;
    color: var(--gold);
    font-size: 33px;
    line-height: 36px;
  }
  .contact {
    position: absolute;
    left: 0;
    right: 0;
    top: 250px;
    text-align: center;
    font-family: "Arimo", sans-serif;
    color: var(--gold);
    font-size: 19px;
    line-height: 26px;
  }
  .web-band {
    position: absolute;
    left: 0;
    right: 0;
    top: 315px;
    height: 26px;
    background: linear-gradient(to right, #8c8c8c, #f4f4f4 35%, #ffffff 55%, #cfcfcf 85%, #9a9a9a);
    text-align: center;
    font-family: "Arimo", sans-serif;
    font-size: 16px;
    line-height: 26px;
    color: var(--ink);
  }
  .back-mark {
    position: absolute;
    inset: 0;
    display: flex;
    align-items: center;
    justify-content: center;
    gap: 20px;
  }
  .back-mark__dot {
    width: 90px;
    height: 90px;
    border-radius: 50%;
    background: var(--silver-dark);
  }
  .back-mark__name {
    font-family: "Arimo", sans-serif;
    font-size: 40px;
    color: var(--silver);
    margin: 0;
  }
</style>
</head>
<body>
  <section class="card card--front">
    <div class="brand">
      <span class="brand__dot"></span>
      <p class="brand__name">Bright<br>Pebblo</p>
    </div>
    <div class="person">
      <div class="person__name">Lena Harbus LMT</div>
      <div class="person__role">Owner</div>
    </div>
    <div class="contact">
      <div class="contact__phone">Phone:555-014-2287</div>
      <div class="contact__email">E-mail:BP@BrightPebblo.com</div>
    </div>
    <div class="web-band">www.brightpebblo.com</div>
  </section>

  <section class="card card--back">
    <div class="back-mark">
      <span class="back-mark__dot"></span>
      <p class="back-mark__name">Bright Pebblo</p>
    </div>
  </section>
</body>
</html>
```